Young judge needs a website to publish and to connect

I would like to have a website where I can publish my articles in public law. I am judge at the Alpine Civic Review Tribunal. Therefore, the website must have a calm, friendly and fairly neutral design. Also, it should be mobile friendly and easy to use.

On my website, I want to

- publish articles such as https://www.brindlepost.example/pulse/how-win-court-tobias-wenger/ and get feedbacks from my colleagues
- generate interest for my project on 'Statutes and Society - Notes from the Chamber', a book that I would like to publish in 2020 and which brings together my publications on public law (http://www.civicnorm.example/content/english/profil/publikationen.html ).
- provide updates for my university courses on constitutional, administrative and international law.

For that purpose, I would kindly ask you to suggest a website that communicates a fresh approach to the work of a young judge in constitutional and administrative law. Please have in mind that I do not only sit on the bench, but that I also work in academia. Therefore, it should be suitable for an audience from both university and law practice. The website should replace the existing website on www.civicnorm.example that I designed when still working as a lawyer. Thank you.

Target Market(s)

Academica, law firms, courts

Industry/Entity Type

University

Contact Information for Business Card

Tobias Wenger
Judge
Alpine Civic Review Tribunal
M +41 79 5XX 8X 2X

Logo Text

Notes from the Chamber

Number of Pages Required

5+ page

Font styles to use
Sans Serif

Colors
0455a3

Requirements
Must have
• - a page where I can publish and get feedbacks
• - a page about my project on Statutes and Society
• - a page where I can provide updates for my university courses on constitutional, administrative and international law
• - page where I can list current and planned projects
• - a collaborative, young and fresh approach
Nice to have
• - a page reserved for my colleagues at the Alpine Civic Review Tribunal where I can alert them about to possibility to collaborate (if possibly password protected) and where they may suggest what to contribute to a specific project
Should not have
• anything which might to suggest that I want to make money with it, bragging or pretentious. Do not forget: I am judge, not a barrister.

```html
<!DOCTYPE html>
<html lang="en">
<head>
<meta charset="utf-8">
<title>Tobias Wenger – Judge &amp; Lecturer</title>
<link rel="stylesheet" href="https://fonts.googleapis.com/css2?family=Open+Sans:wdth,wght@75..100,300..800&display=swap">
<style>
:root{
  --brand:#0455a3;
  --brand-dark:#073f7d;
  --brand-deep:#0a2d5a;
  --sky:#1e88f0;
  --sky-light:#2f95f5;
  --red:#e01b0f;
  --ink:#333;
  --muted:#777;
  --card:#f4f4f4;
  --white:#fff;
}
*{box-sizing:border-box;margin:0;padding:0}
html,body{width:1200px;height:3020px;overflow:hidden}
body{font-family:"Open Sans",Arial,sans-serif;color:var(--ink);background:var(--white);position:relative}
a{color:inherit;text-decoration:none}
.cond{font-stretch:75%}

/* top bar */
.topbar{position:absolute;left:0;top:0;width:1200px;height:40px;background:var(--brand);color:#fff;font-size:14px;display:flex;align-items:center;padding:0 76px}
.topbar .address{display:flex;align-items:center;gap:8px}
.topbar .right{margin-left:auto;display:flex;align-items:center;gap:10px}
.topbar .call{margin-right:16px}
.social-dot{width:22px;height:22px;border-radius:50%;background:var(--sky)}
.lang{margin-left:22px;font-size:12px}
.lang .active{color:#58b3ff}

/* header */
.header{position:absolute;left:0;top:40px;width:1200px;height:86px;display:flex;align-items:center;padding:0 76px}
.logo{font-family:"Open Sans",sans-serif;font-weight:700;font-size:23px;color:var(--brand);font-stretch:85%;letter-spacing:.3px}
.nav{margin-left:auto;display:flex;align-items:center;gap:40px;font-size:15px;color:#222}
.nav .current{color:var(--brand)}
.members{background:var(--red);color:#fff;border-radius:18px;padding:7px 22px;font-size:16px;margin-left:-6px}

/* hero */
.hero{position:absolute;left:0;top:126px;width:1200px;height:646px;background:linear-gradient(180deg,#6e7f95 0%,#3a4f72 45%,#1c2e55 100%)}
.hero-text{position:absolute;left:0;top:272px;width:1200px;text-align:center;color:#fff}
.hero-text h1{font-size:58px;font-weight:700;letter-spacing:.5px;line-height:1}
.hero-text p{font-size:18px;margin-top:10px;color:#e8eef8}
.hero-arrow{position:absolute;top:305px;width:40px;height:40px;border-radius:50%;background:rgba(255,255,255,.25);display:flex;align-items:center;justify-content:center}

/* features */
.features{position:absolute;left:76px;top:876px;width:1048px;height:195px;display:flex}
.feature{flex:1;background:var(--sky);color:#fff;text-align:center;position:relative;padding-top:62px}
.feature.featured{background:var(--brand-dark);height:218px;border-bottom:8px solid var(--sky)}
.feature h3{font-size:28px;font-weight:700;font-stretch:75%}
.feature p{font-size:13px;line-height:1.55;margin:12px auto 0;width:210px}
.feature-icon{position:absolute;left:50%;top:-48px;margin-left:-48px;width:96px;height:96px;border-radius:50%;background:var(--brand-dark);display:flex;align-items:center;justify-content:center}
.featured .feature-icon{background:var(--brand)}

/* profile */
.profile{position:absolute;left:0;top:1162px;width:1200px;height:400px;background:linear-gradient(90deg,#1e3660 0%,#14305e 50%,#0e2750 100%)}
.avatar{position:absolute;left:76px;top:68px;width:266px;height:266px;border-radius:50%;background:radial-gradient(circle at 50% 45%,#d9b59a 0%,#8a7464 45%,#4a4e58 100%);border:6px solid #fff}
.profile .divider{position:absolute;left:372px;top:60px;width:2px;height:280px;background:rgba(255,255,255,.7)}
.profile-body{position:absolute;left:408px;top:58px;width:700px;color:#fff}
.profile-body h2{font-size:26px;font-weight:700;letter-spacing:.3px}
.profile-body .role{color:#3a9bff;font-size:15px;text-transform:uppercase;margin-top:4px}
.profile-body p{font-size:16px;line-height:1.85;margin-top:16px;color:#e9eef6}
.btn-more{display:inline-block;margin-top:26px;background:var(--sky);color:#fff;font-weight:700;font-size:15px;padding:10px 13px;border-radius:5px}

/* articles */
.articles-head{position:absolute;left:0;top:1606px;width:1200px;text-align:center}
.articles-head h2{font-size:26px;color:var(--brand);font-weight:700;font-stretch:75%}
.articles-head p{font-size:20px;color:#8a8a8a;font-weight:300;margin-top:8px}
.article-grid{position:absolute;left:109px;top:1721px;width:980px;display:grid;grid-template-columns:repeat(3,312px);column-gap:22px;row-gap:24px}
.article{background:var(--card);height:308px;padding:22px 22px 0 22px;border:1px solid #ececec}
.article h3{font-size:16px;color:var(--brand);font-weight:700}
.article .date{font-size:11px;color:#666;margin-top:2px}
.article p{font-size:13px;line-height:1.6;color:#555;margin-top:18px;height:84px}
.btn-read{display:inline-flex;align-items:center;gap:10px;margin-top:18px;background:var(--brand);color:#fff;font-size:13px;padding:4px 6px 4px 10px;border-radius:2px}
.meta{display:flex;gap:26px;font-size:11px;color:#555;margin-top:26px}
.meta span{display:flex;align-items:center;gap:5px}

/* pre-order */
.preorder{position:absolute;left:0;top:2413px;width:1200px;height:421px;background:var(--brand)}
.book{position:absolute;left:140px;top:56px;width:300px;height:330px;background:linear-gradient(160deg,#ff6a2a 0%,#e8481a 60%,#b83010 100%);transform:rotate(10deg);border-radius:4px}
.preorder-body{position:absolute;left:485px;top:86px;color:#fff}
.preorder-body h2{font-size:40px;font-weight:500;font-stretch:80%;letter-spacing:.5px}
.preorder-body .lead{font-size:20px;margin-top:2px;font-weight:300}
.form-row{display:flex;gap:20px;margin-top:30px}
.field{width:252px;height:43px;border:1px solid #fff;border-radius:4px;font-size:14px;padding:11px 16px;color:#fff}
.btn-submit{display:inline-block;margin-top:36px;background:var(--red);color:#fff;font-weight:700;font-size:24px;padding:10px 26px;border-radius:3px;letter-spacing:.5px}
.arrow-hint{position:absolute;left:720px;top:278px}

/* footer */
.footer{position:absolute;left:0;top:2834px;width:1200px;height:186px;text-align:center}
.footer-nav{margin-top:38px;font-size:15px;color:#333}
.footer-nav .current{color:var(--brand)}
.footer-nav .sep{margin:0 10px}
.footer-social{display:flex;justify-content:center;gap:10px;margin-top:22px}
.footer-social span{width:28px;height:28px;border-radius:50%;border:2px solid var(--brand)}
.copyright{font-size:13px;color:#888;margin-top:18px}
</style>
</head>
<body>

<div class="topbar">
  <div class="address">
    <svg width="10" height="14" viewBox="0 0 10 14"><path d="M5 0a5 5 0 0 1 5 5c0 4-5 9-5 9S0 9 0 5a5 5 0 0 1 5-5z" fill="#fff"/><circle cx="5" cy="5" r="2" fill="#0455a3"/></svg>
    <span>Lindenweg 24 | PO Box 318 | 8099 Talmatt | Switzerland</span>
  </div>
  <div class="right">
    <span class="call">CALL: +41 44 508 17 63</span>
    <span class="social-dot"></span><span class="social-dot"></span><span class="social-dot"></span><span class="social-dot"></span>
    <span class="lang">DEUTSCH &nbsp;|&nbsp; <span class="active">ENGLISH</span></span>
  </div>
</div>

<header class="header">
  <div class="logo">TOBIAS WENGER</div>
  <nav class="nav">
    <a class="current">HOME</a><a>ABOUT</a><a>ARTICLES</a><a>PROJECT</a><a>COURSES</a><a>CONTACT</a>
    <a class="members">ACRT MEMBERS</a>
  </nav>
</header>

<section class="hero" role="img" aria-label="Photo of graduates in gowns throwing their caps into the sky">
  <div class="hero-arrow" style="left:24px"><svg width="12" height="14" viewBox="0 0 12 14"><path d="M8 2 3 7l5 5" stroke="#fff" stroke-width="2" fill="none"/></svg></div>
  <div class="hero-arrow" style="right:14px"><svg width="12" height="14" viewBox="0 0 12 14"><path d="m4 2 5 5-5 5" stroke="#fff" stroke-width="2" fill="none"/></svg></div>
  <div class="hero-text">
    <h1>TOBIAS WENGER LAW FIRM</h1>
    <p>in-house know-how of law firms by providing specialised expertise</p>
  </div>
</section>

<section class="features">
  <div class="feature">
    <div class="feature-icon"><svg width="44" height="44" viewBox="0 0 44 44"><path d="M12 8h22v24H14a3 3 0 0 0 0 6h20" fill="none" stroke="#fff" stroke-width="3"/><path d="M12 8v27" stroke="#fff" stroke-width="3"/><path d="M17 14h12M17 19h12" stroke="#fff" stroke-width="2"/></svg></div>
    <h3>WHO WE ARE</h3>
    <p>Fusce vulputate tortor sed eros pellentesque pretium vivamus gravida mauris eget.</p>
  </div>
  <div class="feature featured">
    <div class="feature-icon"><svg width="44" height="44" viewBox="0 0 44 44"><path d="M8 12h14v10l-6 6H8z M22 16h14v22H20V28" fill="none" stroke="#fff" stroke-width="2.5"/><path d="M16 28v-6h6" fill="none" stroke="#fff" stroke-width="2"/></svg></div>
    <h3>OUR PROJECTS</h3>
    <p>'Statutes and Society - Notes from the Chamber', a book that I would like to publish in 2020</p>
  </div>
  <div class="feature">
    <div class="feature-icon"><svg width="48" height="32" viewBox="0 0 48 32"><path d="M2 16C10 4 38 4 46 16 38 28 10 28 2 16z" fill="#fff"/><circle cx="24" cy="16" r="8" fill="#073f7d"/><circle cx="24" cy="16" r="4" fill="#fff"/></svg></div>
    <h3>OUR VISION</h3>
    <p>Maecenas rhoncus vulputate est, a finibus nisi posuere quisque vitae commodo mauris.</p>
  </div>
</section>

<section class="profile" role="img" aria-label="Background photo of a courthouse colonnade in dark blue tones">
  <div class="avatar" role="img" aria-label="Portrait photo of Tobias Wenger"></div>
  <div class="divider"></div>
  <div class="profile-body">
    <h2>TOBIAS WENGER RECHTSANWALT</h2>
    <div class="role">Judge, Alpine Civic Review Tribunal</div>
    <p>civicnorm.example offers flexible legal outsourcing of Swiss administrative legal issues for business law firms. Its founder Tobias Wenger provides independent legal consulting services. Tobias's primary focus is on judicial review of administrative action and administrative procedure, but he also provides advice and legal opinions in health and higher education matters...</p>
    <a class="btn-more">READ MORE</a>
  </div>
</section>

<div class="articles-head">
  <h2>LATEST ARTICLES</h2>
  <p>Donec ullamcorper condimentum auctor donec laoreet sit amet tortor cursus mollis</p>
</div>

<section class="article-grid">
  <article class="article">
    <h3>TEMPUS VEL LAOREET VITAE</h3><div class="date">Published on October 24, 2015</div>
    <p>Etiam ut pretium mauris. Maecenas ligula rhoncus vulputate est, a finibus nisi amet posuere quisque vitae commodo mauris. Praesent tincidunt dignissim eros, posuere vestibulum quis.</p>
    <a class="btn-read">Read article <svg width="8" height="10" viewBox="0 0 8 10"><path d="m1 1 3 4-3 4M4 1l3 4-3 4" stroke="#fff" stroke-width="1.4" fill="none"/></svg></a>
    <div class="meta"><span><svg width="11" height="11" viewBox="0 0 11 11"><path d="M0 5h2v6H0zM3 5l3-5c1 0 1.5 1 1 2L6.5 4H10c1 0 1 1 .8 1.5L9.5 10.5H3z" fill="#555"/></svg>Like (48)</span><span><svg width="12" height="11" viewBox="0 0 12 11"><path d="M6 1C2.7 1 0 3 0 5.3 0 6.6.8 7.7 2 8.4L1.5 11l3-2c.5.1 1 .1 1.5.1 3.3 0 6-2 6-4.3S9.3 1 6 1z" fill="#555"/></svg>Comment (9)</span><span><svg width="12" height="10" viewBox="0 0 12 10"><path d="M7 0l5 4.5L7 9V6.3C3.5 6.3 1.5 7.5 0 10 .5 6 3 3.5 7 3z" fill="#555"/></svg>Share (5)</span></div>
  </article>
  <article class="article">
    <h3>HOW TO WIN IN COURT</h3><div class="date">Published on October 24, 2015</div>
    <p>Whereas court proceedings tend to be complicated, judges are not. In fact, they are rather simple creatures. This is why they like it simple. And this is why it is not always that hard to win in court...</p>
    <a class="btn-read">Read article <svg width="8" height="10" viewBox="0 0 8 10"><path d="m1 1 3 4-3 4M4 1l3 4-3 4" stroke="#fff" stroke-width="1.4" fill="none"/></svg></a>
    <div class="meta"><span><svg width="11" height="11" viewBox="0 0 11 11"><path d="M0 5h2v6H0zM3 5l3-5c1 0 1.5 1 1 2L6.5 4H10c1 0 1 1 .8 1.5L9.5 10.5H3z" fill="#555"/></svg>Like (48)</span><span><svg width="12" height="11" viewBox="0 0 12 11"><path d="M6 1C2.7 1 0 3 0 5.3 0 6.6.8 7.7 2 8.4L1.5 11l3-2c.5.1 1 .1 1.5.1 3.3 0 6-2 6-4.3S9.3 1 6 1z" fill="#555"/></svg>Comment (9)</span><span><svg width="12" height="10" viewBox="0 0 12 10"><path d="M7 0l5 4.5L7 9V6.3C3.5 6.3 1.5 7.5 0 10 .5 6 3 3.5 7 3z" fill="#555"/></svg>Share (5)</span></div>
  </article>
  <article class="article">
    <h3>VIVAMUS GRAVIDA MAURIS EGET</h3><div class="date">Published on October 24, 2015</div>
    <p>Proin ac laoreet dui, a rhoncus urna amet Phasellus a pharetra nibh. Integer at risus malesuada felis dignissim rhoncus ut nec quam.Suspendisse orci urna, tempus vel turpis vel, tincidunt egestas ligula.</p>
    <a class="btn-read">Read article <svg width="8" height="10" viewBox="0 0 8 10"><path d="m1 1 3 4-3 4M4 1l3 4-3 4" stroke="#fff" stroke-width="1.4" fill="none"/></svg></a>
    <div class="meta"><span><svg width="11" height="11" viewBox="0 0 11 11"><path d="M0 5h2v6H0zM3 5l3-5c1 0 1.5 1 1 2L6.5 4H10c1 0 1 1 .8 1.5L9.5 10.5H3z" fill="#555"/></svg>Like (48)</span><span><svg width="12" height="11" viewBox="0 0 12 11"><path d="M6 1C2.7 1 0 3 0 5.3 0 6.6.8 7.7 2 8.4L1.5 11l3-2c.5.1 1 .1 1.5.1 3.3 0 6-2 6-4.3S9.3 1 6 1z" fill="#555"/></svg>Comment (9)</span><span><svg width="12" height="10" viewBox="0 0 12 10"><path d="M7 0l5 4.5L7 9V6.3C3.5 6.3 1.5 7.5 0 10 .5 6 3 3.5 7 3z" fill="#555"/></svg>Share (5)</span></div>
  </article>
  <article class="article">
    <h3>TEMPUS VEL LAOREET VITAE</h3><div class="date">Published on October 24, 2015</div>
    <p>Etiam ut pretium mauris. Maecenas ligula rhoncus vulputate est, a finibus nisi amet posuere quisque vitae commodo mauris. Praesent tincidunt dignissim eros, posuere vestibulum quis.</p>
    <a class="btn-read">Read article <svg width="8" height="10" viewBox="0 0 8 10"><path d="m1 1 3 4-3 4M4 1l3 4-3 4" stroke="#fff" stroke-width="1.4" fill="none"/></svg></a>
    <div class="meta"><span><svg width="11" height="11" viewBox="0 0 11 11"><path d="M0 5h2v6H0zM3 5l3-5c1 0 1.5 1 1 2L6.5 4H10c1 0 1 1 .8 1.5L9.5 10.5H3z" fill="#555"/></svg>Like (48)</span><span><svg width="12" height="11" viewBox="0 0 12 11"><path d="M6 1C2.7 1 0 3 0 5.3 0 6.6.8 7.7 2 8.4L1.5 11l3-2c.5.1 1 .1 1.5.1 3.3 0 6-2 6-4.3S9.3 1 6 1z" fill="#555"/></svg>Comment (9)</span><span><svg width="12" height="10" viewBox="0 0 12 10"><path d="M7 0l5 4.5L7 9V6.3C3.5 6.3 1.5 7.5 0 10 .5 6 3 3.5 7 3z" fill="#555"/></svg>Share (5)</span></div>
  </article>
  <article class="article">
    <h3>HOW TO WIN IN COURT</h3><div class="date">Published on October 24, 2015</div>
    <p>Whereas court proceedings tend to be complicated, judges are not. In fact, they are rather simple creatures. This is why they like it simple. And this is why it is not always that hard to win in court...</p>
    <a class="btn-read">Read article <svg width="8" height="10" viewBox="0 0 8 10"><path d="m1 1 3 4-3 4M4 1l3 4-3 4" stroke="#fff" stroke-width="1.4" fill="none"/></svg></a>
    <div class="meta"><span><svg width="11" height="11" viewBox="0 0 11 11"><path d="M0 5h2v6H0zM3 5l3-5c1 0 1.5 1 1 2L6.5 4H10c1 0 1 1 .8 1.5L9.5 10.5H3z" fill="#555"/></svg>Like (48)</span><span><svg width="12" height="11" viewBox="0 0 12 11"><path d="M6 1C2.7 1 0 3 0 5.3 0 6.6.8 7.7 2 8.4L1.5 11l3-2c.5.1 1 .1 1.5.1 3.3 0 6-2 6-4.3S9.3 1 6 1z" fill="#555"/></svg>Comment (9)</span><span><svg width="12" height="10" viewBox="0 0 12 10"><path d="M7 0l5 4.5L7 9V6.3C3.5 6.3 1.5 7.5 0 10 .5 6 3 3.5 7 3z" fill="#555"/></svg>Share (5)</span></div>
  </article>
  <article class="article">
    <h3>VIVAMUS GRAVIDA MAURIS EGET</h3><div class="date">Published on October 24, 2015</div>
    <p>Proin ac laoreet dui, a rhoncus urna amet Phasellus a pharetra nibh. Integer at risus malesuada felis dignissim rhoncus ut nec quam.Suspendisse orci urna, tempus vel turpis vel, tincidunt egestas ligula.</p>
    <a class="btn-read">Read article <svg width="8" height="10" viewBox="0 0 8 10"><path d="m1 1 3 4-3 4M4 1l3 4-3 4" stroke="#fff" stroke-width="1.4" fill="none"/></svg></a>
    <div class="meta"><span><svg width="11" height="11" viewBox="0 0 11 11"><path d="M0 5h2v6H0zM3 5l3-5c1 0 1.5 1 1 2L6.5 4H10c1 0 1 1 .8 1.5L9.5 10.5H3z" fill="#555"/></svg>Like (48)</span><span><svg width="12" height="11" viewBox="0 0 12 11"><path d="M6 1C2.7 1 0 3 0 5.3 0 6.6.8 7.7 2 8.4L1.5 11l3-2c.5.1 1 .1 1.5.1 3.3 0 6-2 6-4.3S9.3 1 6 1z" fill="#555"/></svg>Comment (9)</span><span><svg width="12" height="10" viewBox="0 0 12 10"><path d="M7 0l5 4.5L7 9V6.3C3.5 6.3 1.5 7.5 0 10 .5 6 3 3.5 7 3z" fill="#555"/></svg>Share (5)</span></div>
  </article>
</section>

<section class="preorder">
  <div class="book" role="img" aria-label="Illustration of the orange book cover for Statutes and Society - Notes from the Chamber by Tobias Wenger"></div>
  <div class="preorder-body">
    <h2>STATUTES AND SOCIETY PRE-ORDER!</h2>
    <div class="lead">Enter your name and mobile number below</div>
    <div class="form-row">
      <div class="field">Name</div>
      <div class="field">Email address</div>
    </div>
    <a class="btn-submit">SUBMIT NOW</a>
  </div>
  <svg class="arrow-hint" width="150" height="70" viewBox="0 0 150 70"><path d="M140 8C120 40 80 58 20 48" stroke="#fff" stroke-width="4" fill="none" stroke-linecap="round"/><path d="M34 32 18 48l20 10" stroke="#fff" stroke-width="4" fill="none" stroke-linecap="round" stroke-linejoin="round"/></svg>
</section>

<footer class="footer">
  <div class="footer-nav">
    <a class="current">HOME</a><span class="sep">|</span><a>ABOUT</a><span class="sep">|</span><a>ARTICLES</a><span class="sep">|</span><a>PROJECT</a><span class="sep">|</span><a>COURSES</a><span class="sep">|</span><a>CONTACT</a>
  </div>
  <div class="footer-social"><span></span><span></span><span></span><span></span></div>
  <div class="copyright">Copyright © 2017 civicnorm. All rights reserved.</div>
</footer>

</body>
</html>
```